Nine Moons Brochure Design Project

I need a brochure for my new company "Nine Moons". You can read all about the company at http://www.ninemoons-example.com.sg
On the website you will also get an idea of the concept of the product, as well as design. This design actually comes from a Wordpress theme.
The brochure needs to be like a print version of the website but much more summarised, high-level. I'd like to distribute it to expecting mothers at various locations such as pre-natal yoga classes. The intention is to create enough interest so these moms-to-be will surf to my website and check out what it's all about.
Target Market(s)
Expecting moms and dads (pregnant)
Industry/Entity Type
It Company
Look and feel

```html
<!DOCTYPE html>
<html lang="en">
<head>
<meta charset="utf-8">
<title>Nine Moons Brochure</title>
<link rel="stylesheet" href="https://fonts.googleapis.com/css2?family=Open+Sans:wght@400;600;700&display=swap">
<style>
  :root {
    --page-bg: #e4e4e4;
    --paper: #fbfaf8;
    --brown: #7a4a22;
    --brown-soft: #a8672f;
    --ink: #1c1c1c;
    --skin-light: #efe4df;
    --skin-mid: #c9aba3;
    --beige-light: #f6e7cc;
    --beige: #ead2a6;
    --band: #fdfcfa;
  }
  html, body {
    margin: 0;
    width: 1200px;
    height: 801px;
    overflow: hidden;
    background: var(--page-bg);
    font-family: "Open Sans", Arial, sans-serif;
  }
  .brochure {
    position: absolute;
    left: 320px;
    top: 20px;
    width: 560px;
    height: 760px;
    background: var(--paper);
    overflow: hidden;
    box-shadow: 0 2px 10px rgba(0,0,0,0.15);
  }
  .hero-photo {
    position: absolute;
    inset: 0 0 250px 0;
    background: radial-gradient(ellipse at 35% 70%, var(--skin-mid) 0%, var(--skin-light) 55%, #ffffff 100%);
  }
  .headline {
    position: absolute;
    left: 24px;
    top: 26px;
    width: 250px;
    margin: 0;
    color: var(--brown-soft);
    font-weight: 600;
    line-height: 1.15;
  }
  .headline .kicker { display: block; font-size: 20px; }
  .headline .main { display: block; font-size: 30px; color: var(--brown); font-weight: 700; white-space: nowrap; }
  .intro {
    position: absolute;
    right: 26px;
    top: 26px;
    width: 226px;
    margin: 0;
    text-align: right;
    font-size: 14px;
    line-height: 1.6;
    color: var(--ink);
  }
  .wave {
    position: absolute;
    left: 0;
    top: 410px;
    width: 560px;
    height: 350px;
  }
  .founder-photo {
    position: absolute;
    left: 40px;
    bottom: 0;
    width: 280px;
    height: 200px;
    background: radial-gradient(ellipse at 50% 60%, #c9a778 0%, rgba(234,210,166,0) 70%);
  }
  .founder {
    position: absolute;
    right: 30px;
    top: 540px;
    text-align: right;
    color: var(--brown);
  }
  .founder .name { margin: 0; font-size: 34px; font-weight: 600; }
  .founder .role { margin: 4px 0 0; font-size: 16px; }
  .founder .visit { margin: 30px 0 0; font-size: 15px; color: var(--brown-soft); }
</style>
</head>
<body>
  <article class="brochure">
    <div class="hero-photo" role="img" aria-label="Photo of a pregnant belly with a pair of tiny baby sneakers resting on it"></div>

    <h1 class="headline">
      <span class="kicker">Congratulations!</span>
      <span class="main">You’re pregnant!</span>
    </h1>

    <p class="intro">While everyone else is staring at the ever-growing mountain of to-do lists, you are quietly but steadily piecing together the anticipation of your little one’s arrival. And questions, so many questions that your doctor/midwife just can’t answer for you!</p>

    <svg class="wave" viewBox="0 0 560 350">
      <defs>
        <linearGradient id="beigeFill" x1="0" y1="0" x2="0" y2="1">
          <stop offset="0" stop-color="var(--beige-light)"/>
          <stop offset="1" stop-color="var(--beige)"/>
        </linearGradient>
        <path id="bandLine" d="M 10 120 Q 280 44 560 22"/>
      </defs>
      <path d="M 0 110 Q 280 20 560 0 L 560 44 Q 280 70 0 160 Z" fill="var(--band)"/>
      <path d="M 0 160 Q 280 70 560 44 L 560 350 L 0 350 Z" fill="url(#beigeFill)"/>
      <text font-family="Open Sans, Arial, sans-serif" font-size="14" fill="var(--ink)">
        <textPath href="#bandLine" startOffset="0">From what to buy- to -planning the baby shower. Everything you need.</textPath>
      </text>
    </svg>

    <div class="founder-photo" role="img" aria-label="Photo of the founder with her young daughter"></div>

    <div class="founder">
      <p class="name">Mira Tan</p>
      <p class="role">Founder, Nine Moons</p>
      <p class="visit">or visit ninemoons-example.com.sg</p>
    </div>
  </article>
</body>
</html>
```